Webdesign für Marke KLARWERK plus
Zielgruppe
K+W Zielwertkraft besteht seit 1995 und war zunächst jahrzehntelang als klassische Werbeagentur mit den Schwerpunkten Print, VKF und TV tätig. In den vergangenen Jahren hat sich unsere unternehmerische Ausrichtung jedoch zunehmend auf die Bereiche Expansion, Akquisition und Consulting verlagert –hier sind wir schwerpunktmäßig für zwei große deutsche Unternehmen als etablierter Dienstleister tätig.
Aktuell forcieren wir nun unsere Marke KLARWERK plus. Schwerpunkt von KLARWERK plus ist es, das Thema „Hygiene-Auftritt“ künftig zum Bestandteil einer zukunftsorientierten Unternehmensführung bzw. eines erfolgreichen Marketing-Mix zu machen. Zunächst starten wir mit zwei hochwertigen Varianten von wohl einzigartigen Desinfektionsgeräten, die Qualität, Design und eine hohe Marken- Individualisierbarkeit vereinen. Zielgruppe ist der Gesamtbereich B-to-B.
Aufgabenstellung
Aktuell existiert eine erste Broschüre, die aber nicht zwingend das 'Maß der Dinge' sein muss - wir sind da ganz offen! Diese Broschüre fügen wir als pdf bei. Sie ist sehr kurzfristig auf dei beine gestellt worden, vielleicht ist sie auch 'zu un-emotional' und insofern zu wenig zum Kauf anregend. Dann schlagen SIE doch eine andere Art von Website vor!

```html
<!DOCTYPE html>
<html lang="de">
<head>
<meta charset="utf-8">
<title>KLARWERK plus – Hygienesäulen</title>
<link rel="stylesheet" href="https://fonts.googleapis.com/css2?family=Open+Sans:wght@400;600;700;800&family=Roboto:wght@700&display=swap">
<style>
:root{
  --gold:#cfad4f;
  --gold-light:#e2c96a;
  --ink:#1c1c1c;
  --text:#333;
  --muted:#7a7a7a;
  --soft-bg:#f8f8f8;
  --violet:#8a4a8f;
  --red:#d4232f;
  --teal:#2bb5b0;
  --navy:#1f2f73;
  --white:#fff;
}
*{margin:0;padding:0;box-sizing:border-box}
html,body{width:1200px;height:2340px;overflow:hidden;background:var(--white)}
body{font-family:"Open Sans",Arial,sans-serif;color:var(--text);position:relative}
.topbar{position:absolute;left:0;top:0;width:1200px;height:22px;background:linear-gradient(90deg,var(--gold-light),var(--gold));color:var(--white);font-size:9.5px;font-weight:600}
.topbar .contact{position:absolute;top:5px;display:flex;align-items:center;gap:4px}
.topbar svg{width:10px;height:10px;fill:var(--white)}
.header{position:absolute;left:0;top:22px;width:1200px;height:55px;background:var(--white);box-shadow:0 2px 6px rgba(0,0,0,.06);z-index:2}
.brand{position:absolute;left:30px;top:14px;display:flex;align-items:center;gap:8px;font-weight:800;font-size:24px;letter-spacing:1px;color:var(--ink)}
.brand .mark{width:12px;height:12px;border-radius:50%;background:var(--gold)}
.nav{position:absolute;right:31px;top:29px;display:flex;gap:24px;font-size:9.5px;font-weight:600;color:var(--muted);text-transform:uppercase;letter-spacing:.2px}
.section{position:absolute;left:0;width:1200px}
.section svg.art{position:absolute;left:0;top:0}
.eyebrow{position:absolute;left:102px;font-family:"Roboto",Arial,sans-serif;font-weight:700;font-size:9.5px;text-transform:uppercase}
.title{position:absolute;left:102px;font-weight:700;font-size:25px;line-height:29px;color:var(--ink)}
.copy{position:absolute;left:102px;width:242px;font-size:9.5px;line-height:15.5px;text-align:justify;color:var(--text)}
.copy p+p{margin-top:11px}
.note{position:absolute;left:853px;font-size:9.5px;line-height:15.5px;text-align:justify;color:var(--text)}
.s-lavender{top:77px;height:509px}
.s-bakery{top:586px;height:484px;background:var(--soft-bg)}
.s-theme{top:1070px;height:541px}
.cta{position:absolute;left:0;top:1611px;width:1200px;height:620px;overflow:hidden}
.cta .photo{position:absolute;inset:0;background:linear-gradient(120deg,#d9d2c6 0%,#b9b2a6 35%,#7d8ea4 60%,#c9c2b5 100%)}
.cta h2{position:absolute;left:0;width:1200px;top:222px;text-align:center;font-weight:800;font-size:34px;line-height:43px;color:var(--white);text-transform:uppercase}
.cta .button{position:absolute;left:499px;top:373px;width:202px;height:32px;border-radius:16px;background:linear-gradient(90deg,var(--gold-light),var(--gold));color:var(--white);font-size:8.5px;font-weight:700;letter-spacing:2px;text-transform:uppercase;display:flex;align-items:center;justify-content:center}
.cta svg.wave{position:absolute;left:0;bottom:0}
.footer{position:absolute;left:0;top:2231px;width:1200px;height:109px;background:var(--white)}
.footer .copyright{position:absolute;left:31px;top:40px;font-size:11px;color:var(--muted)}
.footer .brand{left:500px;top:32px}
.footer .legal{position:absolute;right:31px;top:42px;display:flex;gap:31px;font-size:9.5px;font-weight:600;color:var(--muted);text-transform:uppercase}
</style>
</head>
<body>

<div class="topbar">
  <span class="contact" style="left:840px"><svg viewBox="0 0 24 24"><path d="M6.6 10.8a15 15 0 0 0 6.6 6.6l2.2-2.2c.3-.3.7-.4 1-.2 1.1.4 2.3.6 3.6.6.6 0 1 .4 1 1V20c0 .6-.4 1-1 1A17 17 0 0 1 3 4c0-.6.4-1 1-1h3.5c.6 0 1 .4 1 1 0 1.3.2 2.5.6 3.6.1.3 0 .7-.2 1z"/></svg>Service-Nr.: 0800 - 410 5522</span>
  <span class="contact" style="left:1013px"><svg viewBox="0 0 24 24"><path d="M2 5h20v14H2z M2 5l10 8 10-8" fill="none" stroke="#fff" stroke-width="2"/></svg>E-Mail: mail@klarwerkplus.de</span>
</div>

<header class="header">
  <div class="brand"><span>KLARWERK plus</span><span class="mark"></span></div>
  <nav class="nav">
    <span>Mission</span><span>Unsere Hygienesäulen ▾</span><span>Indiviualisierbarkeit</span><span>Mehrwert</span><span>Preise &amp; Optionen</span><span>Kontakt</span>
  </nav>
</header>

<section class="section s-lavender">
  <svg class="art" width="1200" height="509" viewBox="0 0 1200 509">
    <defs>
      <linearGradient id="lavenderTone" x1="0" y1="0" x2="1" y2="1">
        <stop offset="0" stop-color="#9b78b8"/><stop offset="1" stop-color="#6b5a9c"/>
      </linearGradient>
    </defs>
    <rect x="437" y="73" width="345" height="379" fill="url(#lavenderTone)" role="img" aria-label="Premium-Station und Standard-Säule in Gelb und Blau vor einem Lavendelfeld, mit rundem Bodenaufkleber"/>
    <g stroke="var(--gold)" stroke-dasharray="2 3">
      <line x1="511" y1="99" x2="841" y2="99"/><line x1="657" y1="173" x2="841" y2="173"/>
      <line x1="777" y1="263" x2="841" y2="263"/><line x1="536" y1="331" x2="841" y2="331"/>
    </g>
    <g fill="var(--gold)">
      <circle cx="841" cy="99" r="3"/><circle cx="841" cy="173" r="3"/><circle cx="841" cy="263" r="3"/><circle cx="841" cy="331" r="3"/>
      <circle cx="511" cy="99" r="8"/><circle cx="657" cy="173" r="8"/><circle cx="777" cy="263" r="8"/><circle cx="536" cy="331" r="8"/>
    </g>
    <g stroke="#fff" stroke-width="1.6">
      <path d="M507 99h8M511 95v8"/><path d="M653 173h8M657 169v8"/><path d="M773 263h8M777 259v8"/><path d="M532 331h8M536 327v8"/>
    </g>
  </svg>
  <div class="eyebrow" style="top:107px;color:var(--violet)">Die Individual-Line: Beispiel Lavendra</div>
  <h1 class="title" style="top:122px">LAVENDRA DE<br>PROVENCE</h1>
  <div class="copy" style="top:199px">Wie perfekt sich die KLARWERK plus Premium-Station sowie auch die Standard-Säule auf die Corporate Identity von Lavendra de Provence umsetzen lässt, zeigen die nebenstehenden Abbildungen.</div>
  <div class="note" style="top:91px;width:183px">Individual-Gestaltung beider Säulen in den Hausfarben blau und gelb</div>
  <div class="note" style="top:165px;width:183px">Standard-Säule in Sonderfarbe blau mit wertigem Acrylschild im oberen Bereich</div>
  <div class="note" style="top:255px;width:183px">Individuelle, zum Markenauftritt passende Point-of-Sale Materialien</div>
  <div class="note" style="top:323px;width:183px">Premium-Station mit dem Ausstattungs-Detail "Papiertücher" und Papierkorb-Element</div>
</section>

<section class="section s-bakery">
  <svg class="art" width="1200" height="484" viewBox="0 0 1200 484">
    <defs>
      <linearGradient id="wheatTone" x1="0" y1="0" x2="1" y2="1">
        <stop offset="0" stop-color="#e0b45a"/><stop offset="1" stop-color="#cf4a3a"/>
      </linearGradient>
    </defs>
    <rect x="437" y="49" width="362" height="378" fill="url(#wheatTone)" role="img" aria-label="Premium-Station und Standard-Säule in Rot und Weiß vor einem Weizenfeld, mit rundem Bodenaufkleber"/>
    <g stroke="var(--gold)" stroke-dasharray="2 3">
      <line x1="525" y1="71" x2="841" y2="71"/><line x1="657" y1="170" x2="841" y2="170"/><line x1="792" y1="285" x2="841" y2="285"/>
    </g>
    <g fill="var(--gold)">
      <circle cx="841" cy="71" r="3"/><circle cx="841" cy="170" r="3"/><circle cx="841" cy="285" r="3"/>
      <circle cx="525" cy="71" r="8"/><circle cx="657" cy="170" r="8"/><circle cx="792" cy="285" r="8"/>
    </g>
    <g stroke="#fff" stroke-width="1.6"><path d="M521 71h8M525 67v8"/><path d="M653 170h8M657 166v8"/><path d="M788 285h8M792 281v8"/></g>
  </svg>
  <div class="eyebrow" style="top:87px;color:var(--red)">Die Individual-Line: Beispiel "Kornhaus"</div>
  <h2 class="title" style="top:104px">Professionalität in<br>allen Segmenten</h2>
  <div class="copy" style="top:178px">Entsprechend der Philosophie dynamischer Filialketten ist die Entscheidung hin zu hochwertigen KLARWERK plus-Stationen genau der richtige Weg:</div>
  <div class="note" style="top:63px;width:219px">Die Premium-Station komplett im Unternehmens-gebrandeten Look für alle Standorte in frequenzstarken Lagen und somit überall dort, wo einfach auch die Zeit fehlt, um sich z.B. der Kontrolle und Nachbefüllung von Desinfektionsmittel zu widmen.</div>
  <div class="note" style="top:162px;width:219px">Die Standardsäule, die im Vergleich zu den üblichen Säulen anderer Anbieter bereits "Premium" ist und aufgrund ihrer zahlreichen Individualisierungsmöglichkeiten punktgenau sowohl auf die CI des Unternehmens als auch auf regionale Belange maßgeschneidert werden kann.</div>
  <div class="note" style="top:277px;width:219px">Ebenso in jeglicher Hinsicht entsprechend den überregionalen wie regionalen Anforderungen des Unternehmens umsetzbar: Point-of-Sale Medien aller Art, die sich dem Bereich Hygiene-Information und insbesondere der "Kunden-Wegesteuerung" widmen.</div>
</section>

<section class="section s-theme">
  <svg class="art" width="1200" height="541" viewBox="0 0 1200 541">
    <defs>
      <linearGradient id="waterTone" x1="0" y1="0" x2="1" y2="1">
        <stop offset="0" stop-color="#3dbab4"/><stop offset="1" stop-color="#b5e2e2"/>
      </linearGradient>
    </defs>
    <rect x="437" y="76" width="323" height="405" fill="url(#waterTone)" role="img" aria-label="Zwei Premium-Stationen in Flowing-Lines und Splash-Optik vor einer Wasseroberfläche"/>
    <circle cx="882" cy="157" r="70" fill="var(--gold)"/>
    <circle cx="882" cy="157" r="62" fill="#454c51"/>
    <text fill="#fff" font-family="Open Sans, Arial, sans-serif" font-size="7.4" font-weight="600" text-anchor="middle">
      <tspan x="882" y="123">KLARWERK plus Themen-</tspan>
      <tspan x="882" y="134">Stationen: Für alle Unter-</tspan>
      <tspan x="882" y="145">nehmen, die von einer</tspan>
      <tspan x="882" y="156">starken Marke gekoppelt</tspan>
      <tspan x="882" y="167">mit branchenspezifischer</tspan>
      <tspan x="882" y="178">Gestaltung überzeugt</tspan>
      <tspan x="882" y="189">sind. Fragen Sie uns bitte</tspan>
      <tspan x="882" y="200">individuell an!</tspan>
    </text>
    <g stroke="var(--gold)" stroke-dasharray="2 3">
      <line x1="693" y1="293" x2="841" y2="293"/><line x1="657" y1="365" x2="841" y2="365"/><line x1="693" y1="423" x2="841" y2="423"/>
    </g>
    <g fill="var(--gold)">
      <circle cx="841" cy="293" r="3"/><circle cx="841" cy="365" r="3"/><circle cx="841" cy="423" r="3"/>
      <circle cx="693" cy="293" r="8"/><circle cx="657" cy="365" r="8"/><circle cx="693" cy="423" r="8"/>
    </g>
    <g stroke="#fff" stroke-width="1.6"><path d="M689 293h8M693 289v8"/><path d="M653 365h8M657 361v8"/><path d="M689 423h8M693 419v8"/></g>
  </svg>
  <div class="eyebrow" style="top:85px;color:var(--teal)">Premium Line: Themen-Stationen</div>
  <h2 class="title" style="top:103px">Faszinierend<br>anzusehen</h2>
  <div class="copy" style="top:176px">
    <p>Die "Themenserie" innerhalb des KLARWERK plus Portfolios richtet sich insbeson-dere an Entscheider aus unterschiedlichen Branchen, welche von der besonderen "verbalen Kraft" der Marke KLARWERK plus überzeugt sind, gleichzeitig aber die gestalterische Perfektion suchen, um Ihren eigenen Firmenzweck optisch nochmals hervorzuheben und aufzuwerten.</p>
    <p>Als Beispiel für die Zielgruppe der internationalen Schwimmbad- und Sauna-/Thermenbetreiber wurde die Premium-Line in ganz besonderer Optik entwickelt.</p>
    <p>Egal, ob man innerhalb dieser Zielgruppen-Hygienestationen die Flowing-Lines Optik oder die Splash-Optik bevorzugt: Das, was jede Premium-Säule auszeichnet, findet sich auch hier wieder:</p>
  </div>
  <div class="note" style="top:285px;width:183px">Die Ausrichtung auf einen hohen Dauereinsatz mit bis zu 40.000 Besprühungen ohne Wartung und ohne Nachfüllung von Desinfektionsmittel</div>
  <div class="note" style="top:357px;width:183px">Die Selektionsmöglichkeit hinsichtlich Details wie "mit oder ohne Tücher" bzw. "mit oder ohne Papierkorb"</div>
  <div class="note" style="top:415px;width:183px">Ergänzende Medien wie z.B. zum jeweiligen Design passende Bodenstopper, Roll-Up Displays etc.</div>
</section>

<section class="cta">
  <div class="photo" role="img" aria-label="Lächelnde Frau im Videogespräch am Laptop, daneben zwei Hygienesäulen in Gold und Weiß"></div>
  <h2>Gerne stellen wir Ihnen<br>KLARWERK plus online via<br>Videocall vor!</h2>
  <div class="button">Wir beraten Sie gerne</div>
  <svg class="wave" width="1200" height="120" viewBox="0 0 1200 120" preserveAspectRatio="none">
    <path d="M0 58 C250 120 520 80 760 40 C950 8 1100 20 1200 50 L1200 120 L0 120 Z" fill="#9fd9d6"/>
    <path d="M0 72 C250 130 520 96 760 58 C950 28 1100 40 1200 68 L1200 120 L0 120 Z" fill="#fff"/>
  </svg>
</section>

<footer class="footer">
  <div class="copyright">Copyright @2020 K+W Zielwertkraft GmbH</div>
  <div class="brand"><span>KLARWERK plus</span><span class="mark"></span></div>
  <div class="legal"><span>AGB</span><span>Impressum</span><span>Datenschutz</span></div>
</footer>

</body>
</html>
```